QuilloBrezza Business cards

Dear team, I need to get the design file to suit it to our team. The focus of the business card is the Automotive Market and the design must be in black colour and the logo must be in glossy black. On the front of the card I need to get the following info:

- Name and Surname
- Title
- eMail
- Phone Number
- Chattera account
- domain address

```html
<!DOCTYPE html>
<html lang="en">
<head>
<meta charset="utf-8">
<title>QuilloBrezza Business Cards</title>
<link rel="stylesheet" href="https://fonts.googleapis.com/css2?family=Rajdhani:wght@700&family=Roboto:wght@400;700&display=swap">
<style>
  :root {
    --backdrop: #d8d4cd;
    --card-black: #070707;
    --card-graphite: #1d1d1f;
    --brand-red: #e8262b;
    --text-white: #f2f2f2;
    --silver-light: #ffffff;
    --silver-mid: #b9b9bd;
    --silver-dark: #6d6d72;
  }
  * { margin: 0; padding: 0; box-sizing: border-box; }
  html, body {
    width: 900px;
    height: 1200px;
    overflow: hidden;
    background: var(--backdrop);
    font-family: "Roboto", Arial, sans-serif;
  }
  .canvas {
    position: relative;
    width: 900px;
    height: 1200px;
  }
  .card {
    position: absolute;
    left: 95px;
    width: 710px;
    height: 418px;
    border-radius: 22px;
    overflow: hidden;
    background: var(--card-black);
    box-shadow: 0 8px 18px rgba(0, 0, 0, 0.45);
  }
  .card-front { top: 130px; }
  .card-back {
    top: 600px;
    background: linear-gradient(125deg, #262628 0%, var(--card-graphite) 45%, #121213 100%);
  }
  .card-art {
    position: absolute;
    inset: 0;
    width: 710px;
    height: 418px;
  }
  .holder-name {
    position: absolute;
    left: 35px;
    top: 70px;
    font-family: "Rajdhani", "Roboto", sans-serif;
    font-weight: 700;
    font-size: 25px;
    color: var(--brand-red);
    letter-spacing: 0.3px;
  }
  .holder-title {
    position: absolute;
    left: 35px;
    top: 102px;
    font-size: 15px;
    color: var(--text-white);
  }
  .brand {
    position: absolute;
    display: flex;
    align-items: center;
    gap: 10px;
    font-family: "Roboto", Arial, sans-serif;
    font-weight: 700;
    color: var(--brand-red);
    white-space: nowrap;
  }
  .brand-mark {
    display: block;
    background: var(--brand-red);
  }
  .card-front .brand {
    left: 345px;
    top: 58px;
    font-size: 34px;
  }
  .card-front .brand-mark { width: 32px; height: 32px; }
  .card-back .brand {
    left: 113px;
    top: 176px;
    font-size: 52px;
  }
  .card-back .brand-mark { width: 46px; height: 46px; }
  .contact-list {
    position: absolute;
    left: 36px;
    top: 284px;
    list-style: none;
  }
  .contact-item {
    display: flex;
    align-items: center;
    height: 24.7px;
    font-size: 17px;
    color: var(--text-white);
  }
  .contact-icon {
    width: 15px;
    height: 15px;
    margin-right: 12px;
    flex: none;
  }
</style>
</head>
<body>
<main class="canvas">

  <section class="card card-front" aria-label="Business card front">
    <svg class="card-art" viewBox="0 0 710 418" aria-hidden="true">
      <defs>
        <linearGradient id="silver-sweep" x1="0" y1="0" x2="1" y2="0">
          <stop offset="0" stop-color="var(--silver-dark)"/>
          <stop offset="0.3" stop-color="var(--silver-light)"/>
          <stop offset="0.6" stop-color="var(--silver-mid)"/>
          <stop offset="1" stop-color="var(--silver-light)"/>
        </linearGradient>
        <linearGradient id="mesh-tone" x1="0" y1="0" x2="1" y2="0.3">
          <stop offset="0" stop-color="#060606"/>
          <stop offset="0.45" stop-color="#3a3a3c"/>
          <stop offset="1" stop-color="#0c0c0c"/>
        </linearGradient>
        <linearGradient id="lower-panel" x1="0" y1="0" x2="0" y2="1">
          <stop offset="0" stop-color="#2a2a2c"/>
          <stop offset="1" stop-color="#18181a"/>
        </linearGradient>
      </defs>
      <rect width="710" height="418" fill="var(--card-black)"/>
      <path d="M0,160 C150,140 260,200 360,260 C460,320 600,330 710,245 L710,418 L0,418 Z" fill="url(#lower-panel)"/>
      <path role="img" aria-label="Hexagonal metal mesh texture" d="M130,0 C250,60 330,230 500,260 C600,275 680,260 710,240 L710,245 C600,330 460,320 360,260 C260,200 150,140 0,160 L0,0 Z" fill="url(#mesh-tone)" opacity="0.85"/>
      <path d="M0,0 L130,0 C200,35 250,90 290,140 C200,110 100,100 0,110 Z" fill="var(--card-black)"/>
      <path d="M132,0 C250,60 330,230 500,260 C600,275 680,260 710,238" fill="none" stroke="url(#silver-sweep)" stroke-width="7"/>
      <path d="M0,160 C150,140 260,200 360,260 C460,320 600,330 710,245" fill="none" stroke="url(#silver-sweep)" stroke-width="14"/>
      <path d="M0,222 C150,205 260,250 360,305 C460,358 600,385 710,372" fill="none" stroke="url(#silver-sweep)" stroke-width="7"/>
      <path d="M0,168 C150,148 260,208 360,268 C460,328 600,338 710,253 L710,368 C600,381 460,354 360,301 C260,246 150,201 0,218 Z" fill="#0b0b0b"/>
    </svg>

    <h1 class="holder-name">Marco Velardi</h1>
    <p class="holder-title">CEO/Founder</p>

    <div class="brand"><span class="brand-mark"></span>QuilloBrezza.com</div>

    <ul class="contact-list">
      <li class="contact-item">
        <svg class="contact-icon" viewBox="0 0 16 16" aria-hidden="true"><path fill="var(--brand-red)" d="M3.5 1 L6 1 L7 4.5 L5.3 5.8 C6.2 7.8 8.2 9.8 10.2 10.7 L11.5 9 L15 10 L15 12.5 C15 13.9 13.9 15 12.5 15 C6.7 15 1 9.3 1 3.5 C1 2.1 2.1 1 3.5 1 Z"/></svg>
        214-555-0142
      </li>
      <li class="contact-item">
        <svg class="contact-icon" viewBox="0 0 16 16" aria-hidden="true"><rect x="1" y="3" width="14" height="10" rx="1" fill="var(--brand-red)"/><path d="M1.5 3.8 L8 9 L14.5 3.8" fill="none" stroke="#111" stroke-width="1.4"/></svg>
        marco@emailaddress.com
      </li>
      <li class="contact-item">
        <svg class="contact-icon" viewBox="0 0 16 16" aria-hidden="true"><g fill="none" stroke="var(--brand-red)" stroke-width="1.4"><circle cx="8" cy="8" r="6.5"/><ellipse cx="8" cy="8" rx="2.8" ry="6.5"/><path d="M1.5 8 H14.5 M2.5 4.8 H13.5 M2.5 11.2 H13.5"/></g></svg>
        www.yourwebsitehere.com
      </li>
      <li class="contact-item">
        <svg class="contact-icon" viewBox="0 0 16 16" aria-hidden="true"><circle cx="8" cy="8" r="7" fill="var(--brand-red)"/></svg>
        Chattera account
      </li>
    </ul>
  </section>

  <section class="card card-back" aria-label="Business card back">
    <svg class="card-art" viewBox="0 0 710 418" aria-hidden="true">
      <defs>
        <linearGradient id="gloss" x1="0" y1="0" x2="1" y2="1">
          <stop offset="0" stop-color="#ffffff" stop-opacity="0.05"/>
          <stop offset="1" stop-color="#ffffff" stop-opacity="0"/>
        </linearGradient>
      </defs>
      <path d="M380,0 L710,0 L710,418 L620,418 C560,250 480,110 380,0 Z" fill="url(#gloss)"/>
    </svg>
    <div class="brand"><span class="brand-mark"></span>QuilloBrezza.com</div>
  </section>

</main>
</body>
</html>
```